Outdoor Banners for Shopping Center

I need outdoor banners for a small California Shopping Center (Halden Crossway Plaza). You must include the property logo. Each parking lot pole will have 2 banners -- one on each side of the pole so the design should take that into account. Use bright colors… something that will work well with the logo. Size for each banner is 30"w x 96"h. It should be bold and easy to read (if you include any additional text).

Target Market(s)

Middle class shoppers.

Industry/Entity Type

Graphic Design

Font styles to use
Serif
Sans Serif

Requirements
Must have
• The property logo.

```html
<!DOCTYPE html>
<html lang="en">
<head>
<meta charset="utf-8">
<title>Halden Crossway Plaza – Pole Banners</title>
<link href="https://fonts.googleapis.com/css2?family=Nunito:wght@800&family=Open+Sans:wght@800&display=swap" rel="stylesheet">
<style>
  :root {
    --navy: #0a2c9c;
    --gold: #ffd21a;
    --gold-line: #f5c400;
    --panel-top: #d9dddd;
    --panel-bottom: #ffffff;
    --category: #2f6fe8;
    --category-shadow: #0b2f88;
    --sky: #3ee6f5;
    --cloud: #bff5fb;
    --grass: #7ed321;
    --edge: #9a9a9a;
  }
  * { box-sizing: border-box; margin: 0; padding: 0; }
  html, body { width: 843px; height: 1200px; overflow: hidden; background: #ffffff; }
  .canvas { position: relative; width: 843px; height: 1200px; }

  .banner {
    position: absolute;
    top: 0;
    width: 375px;
    height: 1198px;
    border: 1px solid var(--edge);
    border-top: none;
    background: linear-gradient(160deg, var(--panel-top) 0%, var(--panel-bottom) 55%);
    overflow: hidden;
  }
  .banner--left { left: 1px; }
  .banner--right { left: 467px; }

  .top-band {
    position: absolute; left: 0; top: 0; width: 100%; height: 38px;
    background: var(--navy);
  }
  .rule {
    position: absolute; left: 0; width: 100%; height: 5px;
    background: var(--gold-line);
  }
  .rule--top { top: 40px; }
  .rule--bottom { top: 1163px; }

  .brand-mark {
    position: absolute; left: 0; top: 70px; width: 100%;
    display: flex; flex-direction: column; align-items: center; gap: 12px;
  }
  .brand-mark__dot {
    width: 64px; height: 64px; border-radius: 50%;
    background: var(--gold);
  }
  .brand-mark__name {
    font-family: "Open Sans", Arial, sans-serif;
    font-weight: 800;
    font-size: 21px;
    line-height: 1.15;
    color: var(--navy);
    text-align: center;
    letter-spacing: 1px;
  }

  .categories {
    position: absolute; left: 0; top: 284px; width: 100%;
    list-style: none; text-align: center;
  }
  .categories li {
    font-family: "Nunito", "Verdana", sans-serif;
    font-weight: 800;
    font-size: 30px;
    line-height: 73.5px;
    height: 73.5px;
    color: var(--category);
    text-shadow: 1px 1px 0 var(--category-shadow);
    white-space: nowrap;
  }

  .scene {
    position: absolute; left: 0; top: 620px; width: 100%; height: 400px;
    background:
      linear-gradient(180deg, rgba(255,255,255,0) 0%, rgba(255,255,255,0) 15%, var(--cloud) 30%, var(--sky) 65%, var(--sky) 80%, var(--grass) 82%, var(--grass) 100%);
  }

  .footer-band {
    position: absolute; left: 0; top: 1020px; width: 100%; height: 132px;
    background: var(--navy);
    display: flex; flex-direction: column; justify-content: center; align-items: center;
  }
  .footer-band__name {
    font-family: "Open Sans", Arial, sans-serif;
    font-weight: 800;
    font-size: 33px;
    line-height: 52px;
    color: var(--gold);
    text-align: center;
    white-space: nowrap;
  }
</style>
</head>
<body>
<main class="canvas">

  <section class="banner banner--left">
    <div class="top-band"></div>
    <div class="rule rule--top"></div>
    <div class="brand-mark">
      <span class="brand-mark__dot"></span>
      <p class="brand-mark__name">HALDEN CROSSWAY<br>PLAZA</p>
    </div>
    <ul class="categories">
      <li>GROCERY</li>
      <li>VEGETABLES</li>
      <li>FRUITS</li>
      <li>BEVERAGES</li>
    </ul>
    <div class="scene" role="img" aria-label="Illustration of a shopper carrying a pink bag walking on a green hill under a blue sky with a small sun"></div>
    <div class="footer-band">
      <p class="footer-band__name">HALDEN CROSSWAY</p>
      <p class="footer-band__name">PLAZA</p>
    </div>
    <div class="rule rule--bottom"></div>
  </section>

  <section class="banner banner--right">
    <div class="top-band"></div>
    <div class="rule rule--top"></div>
    <div class="brand-mark">
      <span class="brand-mark__dot"></span>
      <p class="brand-mark__name">HALDEN CROSSWAY<br>PLAZA</p>
    </div>
    <ul class="categories">
      <li>STATIONERY</li>
      <li>TOYS</li>
      <li>MUSICS-VIDEOS</li>
      <li>SPORT ACCESORIES</li>
    </ul>
    <div class="scene" role="img" aria-label="Illustration of a shopper carrying a pink bag walking on a green hill under a blue sky with a small sun"></div>
    <div class="footer-band">
      <p class="footer-band__name">HALDEN CROSSWAY</p>
      <p class="footer-band__name">PLAZA</p>
    </div>
    <div class="rule rule--bottom"></div>
  </section>

</main>
</body>
</html>
```